Banner Design for Websites

I am looking for a few various banner designs of the below size. I want them to look authentic, bold and catchy.
Width 939
Height 262
Wording:
WANTED: DRIVEN AND SUCCESSFUL INDIVIDUALS READY TO TAKE THEIR RESULTS TO THE NEXT LEVEL.

Make up to $5000 per sale
No cold calling
No experience required
No pressure selling
NOT MLM

Personal Empowerment. The Next Big Business Boom !

I make well in excess of 10k per month consistently. Brenda K

Some photos attached for use and also some others banners for various workding other than above.

```html
<!DOCTYPE html>
<html lang="en">
<head>
<meta charset="UTF-8">
<title>Personal Development Opportunity Banner</title>
<link href="https://fonts.googleapis.com/css2?family=Lato:ital,wght@0,400;0,700;0,900;1,700;1,900&display=swap" rel="stylesheet">
<style>
  :root{
    --red:#c8000a;
    --red-deep:#a10008;
    --red-bright:#e4141b;
    --violet:#5c5ce6;
    --violet-deep:#3b3bc4;
    --navy:#1f1fa8;
    --headline-blue:#1e1ee8;
    --gold:#f5b400;
    --gold-light:#ffd84a;
    --white:#ffffff;
    --quote-grey:#c9c3e6;
    --button-blue:#3535e0;
  }
  html,body{margin:0;padding:0;overflow:hidden;background:#ffffff;}
  .banner{
    position:relative;width:1200px;height:335px;overflow:hidden;
    font-family:"Lato",Arial,sans-serif;color:var(--white);
  }
  .banner-bg{position:absolute;inset:0;width:1200px;height:335px;}
  .top-bar{position:absolute;left:0;top:0;width:1200px;height:92px;}
  .headline-main{
    position:absolute;left:44px;top:6px;margin:0;
    font-size:72px;font-weight:400;letter-spacing:0.5px;color:var(--headline-blue);
    line-height:80px;
  }
  .headline-divider{position:absolute;left:510px;top:14px;width:2px;height:62px;background:rgba(255,255,255,.55);}
  .headline-sub{
    position:absolute;left:552px;top:18px;margin:0;
    font-size:25px;font-weight:900;line-height:29px;color:var(--white);
  }
  .question{
    position:absolute;top:100px;margin:0;font-size:16.5px;font-weight:900;line-height:20px;
  }
  .question-align{left:38px;width:320px;}
  .question-ready{left:390px;width:330px;}
  .question-divider{position:absolute;left:364px;top:104px;width:1px;height:52px;background:rgba(255,255,255,.45);}
  .glow-line{
    position:absolute;left:20px;top:172px;width:650px;height:3px;
    background:linear-gradient(90deg,rgba(255,255,255,0),rgba(255,255,255,.9) 45%,rgba(255,255,255,0));
  }
  .tick{position:absolute;left:150px;top:188px;width:108px;height:98px;}
  .benefits{
    position:absolute;left:265px;top:182px;margin:0;padding:0;list-style:none;
    font-size:21px;font-weight:700;line-height:24px;
  }
  .photo-frame{position:absolute;left:665px;top:92px;width:240px;height:243px;}
  .quote{
    position:absolute;left:952px;top:110px;width:235px;margin:0;
    font-size:18.5px;font-weight:700;font-style:italic;line-height:23px;
  }
  .quote-mark{position:absolute;font-size:70px;font-weight:900;font-style:italic;color:var(--quote-grey);line-height:1;}
  .quote-open{left:902px;top:92px;}
  .quote-close{left:1150px;top:186px;}
  .cta{
    position:absolute;left:975px;top:266px;width:178px;height:56px;box-sizing:border-box;
    background:var(--button-blue);border:2px dashed var(--white);
    text-align:center;text-decoration:none;color:var(--white);
  }
  .cta-main{display:block;font-size:23px;font-weight:900;line-height:26px;margin-top:4px;}
  .cta-sub{display:block;font-size:13px;font-weight:700;line-height:15px;}
</style>
</head>
<body>
<div class="banner">
  <svg class="banner-bg" viewBox="0 0 1200 335" preserveAspectRatio="none" aria-hidden="true">
    <defs>
      <linearGradient id="violetFill" x1="0" y1="0" x2="0" y2="1">
        <stop offset="0" stop-color="var(--violet)"/>
        <stop offset="1" stop-color="var(--violet-deep)"/>
      </linearGradient>
      <linearGradient id="redFill" x1="0" y1="0" x2="1" y2="1">
        <stop offset="0" stop-color="var(--red-bright)"/>
        <stop offset="1" stop-color="var(--red-deep)"/>
      </linearGradient>
    </defs>
    <rect width="1200" height="335" fill="url(#redFill)"/>
    <path d="M0 92 H1200 V92 C1080 120 960 170 890 230 L785 335 H0 Z" fill="url(#violetFill)"/>
    <path d="M0 322 C150 300 420 290 720 300 L760 335 H0 Z" fill="var(--navy)"/>
    <path d="M0 335 C200 312 460 304 720 315 L735 335 Z" fill="var(--red)"/>
    <path d="M1200 92 C1080 120 960 170 890 230" fill="none" stroke="var(--gold-light)" stroke-width="4"/>
  </svg>

  <svg class="top-bar" viewBox="0 0 1200 92" aria-hidden="true">
    <defs>
      <linearGradient id="barFill" x1="0" y1="0" x2="0" y2="1">
        <stop offset="0" stop-color="var(--red-bright)"/>
        <stop offset="1" stop-color="var(--red-deep)"/>
      </linearGradient>
    </defs>
    <rect width="1200" height="88" fill="url(#barFill)"/>
    <rect y="88" width="1200" height="4" fill="rgba(0,0,0,.25)"/>
  </svg>

  <h1 class="headline-main">PASSIONATE</h1>
  <span class="headline-divider"></span>
  <h2 class="headline-sub">ABOUT PERSONAL DEVELOPMENT/<br>LEADERSHIP DEVELOPMENT?</h2>

  <p class="question question-align">LOOKING TO ALIGN YOURSELF<br>WITH AN OPPORTUNITY OF<br>SUBSTANCE?</p>
  <span class="question-divider"></span>
  <p class="question question-ready">READY TO BE CHALLENGED &amp;<br>ENCOURAGED TO REACH NEW<br>LEVELS OF SUCCESS?</p>
  <span class="glow-line"></span>

  <svg class="tick" viewBox="0 0 108 98" aria-hidden="true">
    <path d="M2 58 L24 46 L40 70 L94 2 L106 10 L42 96 Z" fill="var(--gold)" stroke="#b07c00" stroke-width="2" stroke-linejoin="round"/>
    <path d="M8 58 L24 50 L40 74 L94 8" fill="none" stroke="var(--gold-light)" stroke-width="3"/>
  </svg>

  <ul class="benefits">
    <li>Opportunity for "Big Thinker"</li>
    <li>No cold calling</li>
    <li>Simple Success Formula</li>
    <li>Home Based</li>
    <li>NOT MLM</li>
  </ul>

  <svg class="photo-frame" viewBox="0 0 240 243" role="img" aria-label="Circular portrait photo area">
    <defs>
      <linearGradient id="ringFill" x1="0" y1="1" x2="1" y2="0">
        <stop offset="0" stop-color="var(--navy)"/>
        <stop offset=".6" stop-color="var(--violet)"/>
        <stop offset="1" stop-color="var(--gold-light)"/>
      </linearGradient>
    </defs>
    <circle cx="120" cy="123" r="114" fill="var(--white)" stroke="url(#ringFill)" stroke-width="5"/>
  </svg>

  <span class="quote-mark quote-open">“</span>
  <p class="quote">Let us show you how we've taught others like you to make a quantum leap in their personal results</p>
  <span class="quote-mark quote-close">”</span>

  <a class="cta" href="#">
    <span class="cta-main">CLICK HERE</span>
    <span class="cta-sub">FOR FREE INFO</span>
  </a>
</div>
</body>
</html>
```